Dorvo Letterhead

Hi I really like the attached pictures for our business cards could you please look at designing something similar for our letterheads and stationary.

The details on our letterhead will be

Dorvo Pty Ltd
ABN 418 276 530
PO Box 7214
Kellan Ridge NSW 2871
0472 318 605
office"dorvo.com.au

```html
<!DOCTYPE html>
<html lang="en">
<head>
<meta charset="utf-8">
<title>Dorvo Letterhead</title>
<link href="https://fonts.googleapis.com/css2?family=Montserrat:wght@800&family=Roboto:wght@400;500;700&family=Great+Vibes&display=swap" rel="stylesheet">
<style>
  :root{
    --stage:#4d5155;
    --paper:#f1f1f1;
    --blue:#3f72b8;
    --blue-mid:#2f5a9a;
    --navy:#14203a;
    --accent:#2a8fd6;
    --ink:#222;
    --body:#6b6b6b;
    --rule:#1a1a1a;
  }
  *{margin:0;padding:0;box-sizing:border-box}
  html,body{width:1200px;height:749px;overflow:hidden;background:var(--stage);font-family:"Roboto",sans-serif}
  .stage{position:relative;width:1200px;height:749px}

  /* Letterhead */
  .letterhead{position:absolute;left:171px;top:111px;width:373px;height:526px;background:var(--paper);overflow:hidden}
  .letterhead .header-wave{position:absolute;left:0;top:0}
  .company-block{position:absolute;right:24px;top:18px;text-align:right;color:#fff}
  .company-name{font-family:"Montserrat",sans-serif;font-weight:800;font-size:10px;letter-spacing:.3px}
  .abn{font-size:5.5px;margin-top:1px}
  .abn span{color:#7fc0f0}
  .contact{font-size:6.2px;line-height:8.8px}
  .contact-list{margin-top:5px}
  .contact-row{display:flex;justify-content:flex-end;align-items:center;gap:4px}
  .contact-row svg{width:5px;height:5px;flex:none}

  .wordmark{position:absolute;font-family:"Roboto",sans-serif;font-weight:700;color:var(--ink);letter-spacing:1px}
  .letterhead .wordmark{left:21px;top:74px;font-size:32px}

  .letter{position:absolute;left:23px;top:162px;width:326px;font-size:5.4px;color:var(--body);line-height:8.4px}
  .letter .date{margin-bottom:16px}
  .recipient strong{font-weight:700;color:#555}
  .salutation{margin:14px 0 10px}
  .letter p.body-copy{text-align:justify;margin-bottom:8.5px}
  .sign-off{margin-top:30px}
  .sign-off .name{font-weight:700;color:#555}
  .signature{font-family:"Great Vibes",cursive;font-size:15px;color:#3a4f86;margin:4px 0 0 -8px;line-height:16px}

  /* Envelope front */
  .envelope-front{position:absolute;left:578px;top:161px;width:450px;height:203px;background:var(--paper);overflow:hidden}
  .pattern-panel{position:absolute;left:0;top:0;width:190px;height:203px;background:linear-gradient(135deg,var(--blue) 0%,var(--blue-mid) 60%,#243f70 100%)}
  .envelope-front .wordmark{right:28px;top:20px;font-size:28px}
  .envelope-front .company-block{right:29px;top:134px;color:#222}
  .envelope-front .company-name{color:var(--accent);font-size:9.6px}
  .envelope-front .abn{color:#333}
  .envelope-front .abn span{color:var(--accent)}
  .envelope-front .contact-list{margin-top:4px}

  /* Envelope back */
  .envelope-back{position:absolute;left:578px;top:389px;width:450px;height:202px;background:var(--paper);overflow:hidden}
  .envelope-back .flap{position:absolute;left:0;top:0}
  .flap-url{position:absolute;left:0;right:0;top:34px;text-align:center;color:#fff;font-size:6px;letter-spacing:3.2px}
</style>
</head>
<body>
<div class="stage">

  <section class="letterhead">
    <svg class="header-wave" width="373" height="100" viewBox="0 0 373 100">
      <defs>
        <linearGradient id="waveFill" x1="0" y1="0" x2="0" y2="1">
          <stop offset="0" stop-color="#4a7cc2"/>
          <stop offset=".6" stop-color="#2c5391"/>
          <stop offset="1" stop-color="#17284a"/>
        </linearGradient>
      </defs>
      <path d="M0,0 H373 V80 C330,84 270,70 200,38 C130,6 60,2 0,16 Z" fill="url(#waveFill)"/>
      <path d="M0,16 C60,2 130,6 200,38 C270,70 330,84 373,80" fill="none" stroke="var(--rule)" stroke-width="3.2"/>
      <path d="M0,21 C60,8 130,12 200,44 C270,76 330,90 373,86" fill="none" stroke="#bbb" stroke-width=".6"/>
    </svg>

    <div class="company-block">
      <div class="company-name">DORVO PTY LTD</div>
      <div class="abn"><span>ABN</span> 418 276 530</div>
      <div class="contact-list contact">
        <div class="contact-row">PO Box 7214 Kellan Ridge NSW 2871
          <svg viewBox="0 0 10 10"><path d="M2 1l2 2-1 1.5c.8 1.5 1.8 2.5 3.3 3.3L7.8 6.8l2 2-1.2 1.2C4.5 9.5.5 5.5 0 1.4Z" fill="#7fc0f0"/></svg>
        </div>
        <div class="contact-row">www.dorvo.com.au
          <svg viewBox="0 0 10 10"><circle cx="5" cy="5" r="4.3" fill="#7fc0f0"/></svg>
        </div>
        <div class="contact-row">0472 318 605
          <svg viewBox="0 0 10 10"><path d="M5 0a3.5 3.5 0 0 1 3.5 3.5C8.5 6 5 10 5 10S1.5 6 1.5 3.5A3.5 3.5 0 0 1 5 0Z" fill="#7fc0f0"/></svg>
        </div>
      </div>
    </div>

    <div class="wordmark">DORVO</div>

    <div class="letter">
      <div class="date">30/20/2016</div>
      <div class="recipient">
        <strong>Mr. XYZ Smith</strong><br>
        123, Street No. 123,<br>
        City Name<br>
        Pincode-123456
      </div>
      <div class="salutation">Dear Sir,</div>
      <p class="body-copy">Lorem Ipsum is simply dummy text of the printing and typesetting industry. Lorem Ipsum has been the industry's standard dummy text ever since the 1500s, when an unknown printer took a galley of type and scrambled it to make a type specimen book. It has survived not only five centuries, but also the leap into electronic typesetting, remaining essentially unchanged. It was popularised in the 1960s with the release of Letraset sheets containing Lorem Ipsum passages, and more recently with desktop publishing software like Aldus PageMaker including versions of Lorem Ipsum.</p>
      <p class="body-copy">Lorem Ipsum is simply dummy text of the printing and typesetting industry. Lorem Ipsum has been the industry's standard dummy text ever since the 1500s, when an unknown printer took a galley of type and scrambled it to make a type specimen book. It has survived not only five centuries, but also the leap into electronic typesetting, remaining essentially unchanged. It was popularised in the 1960s with the release of Letraset sheets containing Lorem Ipsum passages, and more recently with desktop publishing software like Aldus PageMaker including versions of Lorem Ipsum.</p>
      <p class="body-copy">Lorem Ipsum is simply dummy text of the printing and typesetting industry. Lorem Ipsum has been the industry's standard dummy text ever since the 1500s, when an unknown printer took a galley of type and scrambled it to make a type specimen book.</p>
      <div class="sign-off">
        <div class="name">Your Name</div>
        <div class="signature">Your Signature</div>
        <div>CEO &nbsp;|&nbsp; Owner</div>
      </div>
    </div>
  </section>

  <section class="envelope-front">
    <div class="pattern-panel" role="img" aria-label="Blue patterned panel"></div>
    <div class="wordmark">DORVO</div>
    <div class="company-block">
      <div class="company-name">DORVO PTY LTD</div>
      <div class="abn"><span>ABN</span> 418 276 530</div>
      <div class="contact-list contact">
        <div class="contact-row">0472 318 605
          <svg viewBox="0 0 10 10"><path d="M2 1l2 2-1 1.5c.8 1.5 1.8 2.5 3.3 3.3L7.8 6.8l2 2-1.2 1.2C4.5 9.5.5 5.5 0 1.4Z" fill="var(--accent)"/></svg>
        </div>
        <div class="contact-row">www.dorvo.com.au
          <svg viewBox="0 0 10 10"><circle cx="5" cy="5" r="4.3" fill="var(--accent)"/></svg>
        </div>
        <div class="contact-row">PO Box 7214 Kellan Ridge NSW 2871
          <svg viewBox="0 0 10 10"><path d="M5 0a3.5 3.5 0 0 1 3.5 3.5C8.5 6 5 10 5 10S1.5 6 1.5 3.5A3.5 3.5 0 0 1 5 0Z" fill="var(--accent)"/></svg>
        </div>
      </div>
    </div>
  </section>

  <section class="envelope-back">
    <svg class="flap" width="450" height="80" viewBox="0 0 450 80">
      <defs>
        <linearGradient id="flapFill" x1="0" y1="0" x2="0" y2="1">
          <stop offset="0" stop-color="#4a7cc2"/>
          <stop offset=".55" stop-color="#2a4f8c"/>
          <stop offset="1" stop-color="#121c33"/>
        </linearGradient>
      </defs>
      <path d="M0,0 H450 L423,58 Q414,73 392,73 H58 Q36,73 27,58 Z" fill="url(#flapFill)"/>
    </svg>
    <div class="flap-url">www.dorvo.com.au</div>
  </section>

</div>
</body>
</html>
```